VelMarkory-Tagsworthly Partial Redesign - Web App

Are you able to apply your creativity to an existing layout? I’m convinced that even just a few touches can make a big difference to add personality and professionalism to a website design, and I’m looking for someone able to use existing ideas and bring them to the next level while keeping inside some given constraints.
The actual job is to improve an existing design concept and to apply it creatively to a landing page, a simple home page, and an older web app (single page website).
To help you start with a clear picture of the current situation and of my requirements, I created a detailed brief with screenshots, live examples, and complete instructions. You can find it attached to this job.
My tastes are inclined towards clean and simple designs. For this project I'm not looking for dazzling novelty, but for very solid craftsmanship. Are the right man - or woman - for the job?
Updates
I wanted to thank everybody who participated in this project. I made a choice, but also other designs were interesting. Hope to work with you another time.
Target Market(s)
Our main target is social media marketers and startuppers
Look and feel
Each slider illustrates characteristics of the customer's brand and the style your logo design should communicate.

```html
<!DOCTYPE html>
<html lang="en">
<head>
<meta charset="utf-8">
<title>Tagsworthly – Exploring #me</title>
<link rel="stylesheet" href="https://fonts.googleapis.com/css2?family=Arimo:wght@400;700&family=Noto+Serif&display=swap">
<style>
:root{
  --bar:#262626;--bar-hi:#3a3a3a;--btn:#3d3d3d;--btn-line:#555;
  --page:#f2f2f2;--card:#fff;--ink:#222;--muted:#bbb;--link:#2f8ac4;
  --the:#3a8fc9;--blue:#aed0e8;--teal:#cde3df;--pale:#f0f0f0;--grey:#9a9a9a;
  --tab:#b9b9b9;--tab-dark:#9c9c9c;--pro:#2a93c9;--rule:#dcdcdc;
}
*{box-sizing:border-box;margin:0;padding:0}
html,body{width:1200px;height:1172px;overflow:hidden;background:var(--page)}
body{font-family:"Arimo",Arial,sans-serif;color:var(--ink)}
.stage{width:1020px;height:996px;position:relative;transform:scale(1.17647);transform-origin:0 0;overflow:hidden;background:var(--page)}
.abs{position:absolute}
.topbar{left:0;top:0;width:1020px;height:52px;background:linear-gradient(var(--bar-hi),var(--bar))}
.brand{left:84px;top:15px;display:flex;align-items:center;gap:8px;color:#fff;font-weight:700;font-size:17px}
.brand-mark{width:20px;height:20px;background:#fff}
.nav-btn{top:12px;height:31px;background:var(--btn);border:1px solid var(--btn-line);border-radius:4px;color:#fff;font-size:14px;display:flex;align-items:center;justify-content:center;gap:6px}
.nav-btn.home{background:#111;border-color:#111}
.account{left:890px;top:18px;color:#fff;font-size:14px;display:flex;gap:10px;align-items:center}
.title{left:49px;top:78px;font-size:25px;color:#333}
.title b,.tag{color:var(--link);font-weight:400}
.tabs{left:40px;top:118px;display:flex;gap:4px}
.tab{display:flex;height:30px;border-radius:3px;overflow:hidden;font-size:13px;color:#fff}
.tab span{padding:0 7px;display:flex;align-items:center;background:var(--tab)}
.tab span+span{border-left:1px solid #d6d6d6}
.tab.on span{background:var(--tab-dark)}
.tab .pro{background:var(--pro)!important}
.sub{left:49px;top:203px;font-size:18px;color:#333}
.hint{left:50px;top:233px;font-size:12px;font-style:italic;color:var(--muted)}
.card{left:40px;top:270px;width:620px;height:740px;background:var(--card);border-radius:6px}
.graph{left:0;top:0}
.graph text{font-family:"Arimo",Arial,sans-serif;font-size:13px;text-anchor:middle;dominant-baseline:central;fill:#222}
.share{left:680px;top:76px;display:flex;gap:4px;font-size:11px;align-items:center}
.share .b{height:21px;padding:0 8px;border-radius:3px;color:#fff;font-weight:700;display:flex;align-items:center}
.share .n{height:21px;padding:0 6px;border:1px solid #ccc;background:#fff;display:flex;align-items:center;margin-right:6px}
.rule{left:680px;width:300px;height:1px;background:var(--rule)}
.pop{left:680px;top:138px;font-size:18px}
.pop b{color:var(--link);font-weight:400}
.search{left:680px;top:171px;width:226px;height:32px;background:#fff;border:1px solid #ddd;border-radius:3px;font-size:13px;color:#aaa;padding:8px 10px}
.search-btn{left:909px;top:171px;width:71px;height:32px;background:#333;color:#fff;border-radius:3px;font-size:14px;display:flex;align-items:center;justify-content:center}
.found{left:680px;top:248px;font-size:18px}
.digits{left:680px;top:280px;display:flex;gap:3px;font-family:"Noto Serif",serif;font-size:18px}
.digits span{width:21px;height:25px;background:#fff;border:1px solid #ddd;border-radius:2px;display:flex;align-items:center;justify-content:center}
.digits span.c{border:none;background:none;width:14px}
.count{left:680px;top:319px;font-size:12px}
.recent{left:680px;top:376px;font-size:18px}
.tweets{left:680px;top:420px;width:300px;list-style:none}
.tweets li{display:flex;gap:8px;font-size:12px;line-height:18px;margin-bottom:10px}
.avatar{flex:none;width:26px;height:26px;margin-top:4px}
.who,.h{color:var(--link)}
.ago{color:var(--muted);font-style:italic}
</style>
</head>
<body>
<div class="stage">
  <header class="topbar abs"></header>
  <div class="brand abs"><span class="brand-mark"></span>VelMarkory</div>
  <div class="nav-btn home abs" style="left:201px;width:50px">
    <svg width="14" height="13" viewBox="0 0 14 13"><path d="M7 0 0 6h2v7h4V9h2v4h4V6h2z" fill="#fff"/></svg>
  </div>
  <div class="nav-btn abs" style="left:259px;width:86px">Products <svg width="8" height="5"><path d="M0 0h8L4 5z" fill="#fff"/></svg></div>
  <div class="nav-btn abs" style="left:698px;width:50px">Blog</div>
  <div class="nav-btn abs" style="left:756px;width:49px">About</div>
  <div class="nav-btn abs" style="left:813px;width:48px">Help</div>
  <div class="account abs"><svg width="14" height="15" viewBox="0 0 14 15"><circle cx="7" cy="4" r="4" fill="#fff"/><path d="M0 15c0-5 3-6 7-6s7 1 7 6z" fill="#fff"/></svg>Account</div>

  <h1 class="title abs" style="font-weight:400">Exploring: <b>#me</b></h1>
  <nav class="tabs abs">
    <div class="tab on"><span>Top Related Hashtags</span><span>Free</span></div>
    <div class="tab"><span>Top Influencers</span><span>Free</span></div>
    <div class="tab"><span>Variants</span><span>Free</span></div>
    <div class="tab"><span>In-Depth Intelligence</span><span class="pro">Pro</span></div>
  </nav>
  <h2 class="sub abs" style="font-weight:400">The top 10 related hashtags for <span class="tag">#me</span></h2>
  <p class="hint abs">To explore the hashtagspace, click on a ball.</p>
  <div class="card abs"></div>

  <svg class="graph abs" width="1020" height="996" viewBox="0 0 1020 996">
    <g stroke="#eeeeee" stroke-width="5">
      <line x1="297" y1="506" x2="289" y2="338"/><line x1="297" y1="506" x2="358" y2="392"/>
      <line x1="297" y1="506" x2="224" y2="412"/><line x1="297" y1="506" x2="97" y2="421"/>
      <line x1="297" y1="506" x2="156" y2="528"/><line x1="297" y1="506" x2="469" y2="527"/>
    </g>
    <g stroke="#8dbde0" stroke-width="6" opacity=".75">
      <line x1="451" y1="683" x2="424" y2="450"/><line x1="451" y1="683" x2="576" y2="562"/>
      <line x1="451" y1="683" x2="231" y2="623"/><line x1="451" y1="683" x2="119" y2="739"/>
      <line x1="451" y1="683" x2="269" y2="765"/><line x1="451" y1="683" x2="364" y2="800"/>
      <line x1="451" y1="683" x2="179" y2="843"/><line x1="451" y1="683" x2="586" y2="767"/>
      <line x1="451" y1="683" x2="514" y2="884"/><line x1="451" y1="683" x2="156" y2="528"/>
      <line x1="451" y1="683" x2="469" y2="527"/>
    </g>
    <line x1="451" y1="683" x2="297" y2="506" stroke="var(--grey)" stroke-width="14"/>
    <g fill="var(--pale)">
      <circle cx="289" cy="338" r="33"/><circle cx="358" cy="392" r="33"/>
      <circle cx="224" cy="412" r="33"/><circle cx="97" cy="421" r="33"/>
    </g>
    <g fill="var(--teal)"><circle cx="156" cy="528" r="33"/><circle cx="469" cy="527" r="33"/></g>
    <g fill="var(--blue)" opacity=".95">
      <circle cx="424" cy="450" r="52"/><circle cx="576" cy="562" r="52"/>
      <circle cx="231" cy="623" r="52"/><circle cx="119" cy="739" r="52"/>
      <circle cx="269" cy="765" r="52"/><circle cx="364" cy="800" r="52"/>
      <circle cx="179" cy="843" r="52"/><circle cx="586" cy="767" r="52"/>
      <circle cx="514" cy="884" r="52"/>
    </g>
    <circle cx="297" cy="506" r="56" fill="var(--grey)"/>
    <circle cx="451" cy="683" r="88" fill="var(--the)"/>
    <text x="289" y="338">to</text><text x="358" y="392">you</text><text x="224" y="412">in</text>
    <text x="97" y="421">people</text><text x="156" y="528">tweet</text><text x="469" y="529">like</text>
    <text x="424" y="451">in</text><text x="576" y="562">use</text><text x="231" y="624">you</text>
    <text x="119" y="739">in</text><text x="269" y="766">people</text><text x="364" y="800">tweet</text>
    <text x="179" y="843">to</text><text x="586" y="767">in</text><text x="514" y="884">people</text>
    <text x="297" y="508" font-weight="700">hashtags</text>
    <text x="449" y="684" font-weight="700">the</text>
  </svg>

  <div class="share abs">
    <span class="b" style="background:#3a9bd6">Chirp</span><span class="n">357</span>
    <span class="b" style="background:#4b67a1">Share</span><span class="n">83</span>
    <span class="b" style="background:#e9e9e9;color:#c33;border:1px solid #ccc">+1</span><span class="n">63</span>
  </div>
  <div class="rule abs" style="top:117px"></div>
  <p class="pop abs">Popularity: <b>73.6</b></p>
  <div class="search abs">eg. banana</div>
  <div class="search-btn abs">Search</div>
  <div class="rule abs" style="top:228px"></div>
  <p class="found abs">Hashtags found so far:</p>
  <div class="digits abs"><span>1</span><span>0</span><span class="c">,</span><span>6</span><span>1</span><span>1</span><span class="c">,</span><span>2</span><span>4</span><span>1</span></div>
  <p class="count abs">in 567,419,411 tweets</p>
  <div class="rule abs" style="top:352px"></div>
  <p class="recent abs">Top recent tweets</p>
  <ul class="tweets abs">
    <li><span class="avatar" role="img" aria-label="User avatar" style="background:#1a7fd8"></span><p><span class="who">JuneLaneTV:</span> RT <span class="h">@DropBoulevard</span>: I hate people on chirper who always have to do <span class="h">#three #unnecessary #hashtags</span> <span class="ago">a minute ago</span></p></li>
    <li><span class="avatar" role="img" aria-label="User avatar" style="background:linear-gradient(#c9a35a,#3b3f6a)"></span><p><span class="who">mireko44:</span> I wonder why people have to put <span class="h">#hashtags</span> on <span class="h">#PB</span>. <span class="ago">2 minutes ago</span></p></li>
    <li><span class="avatar" role="img" aria-label="User avatar" style="background:#8a7a7a"></span><p><span class="who">Tessa_Marie27:</span> My favorite part of Chirper <span class="h">#hashtags</span> <span class="ago">5 minutes ago</span></p></li>
    <li><span class="avatar" role="img" aria-label="User avatar" style="background:#a98a90"></span><p><span class="who">danfordrayyy:</span> <span class="h">@lorabeck</span> 4-12 black FEIDAY <span class="h">#blackfeiday #BLACKFRIDAYMADNESS #baristaproblems #hashtags</span> <span class="ago">5 minutes ago</span></p></li>
    <li><span class="avatar" role="img" aria-label="User avatar" style="background:#f0b05a"></span><p><span class="who">milesvantoni:</span> <span class="h">#Count #Your #Hashtags -- #AndMore</span>: <span class="h">http://chr.pr/q8TzLnWa</span> ~ via <span class="h">@BayNOVUMA</span> <span class="ago">6 minutes ago</span></p></li>
    <li><span class="avatar" role="img" aria-label="User avatar" style="background:linear-gradient(#e0a040,#6a4a3a)"></span><p><span class="who">ClumsyTed:</span> <span class="h">@Q7_K9X</span> part of me doesnt understand.... but the other part of me understands too much <span class="h">#deepthoughts</span> <span class="ago">8 minutes ago</span></p></li>
    <li><span class="avatar" role="img" aria-label="User avatar" style="background:#4a9ae8"></span><p><span class="who">Deni_Lo:</span> <span class="h">@owenpardie4</span> did you have it teed up ?:/ sorry I didn't click on... <span class="h">#failure #killmyself #death #sadness #hashtags</span> <span class="ago">8 minutes ago</span></p></li>
    <li><span class="avatar" role="img" aria-label="User avatar" style="background:radial-gradient(#fff,#8aa8d8)"></span><p><span class="who">rickolmeda:</span> to <span class="h">#getmorefollowers</span> instantly ,follow <span class="h">#hashtags #TeamFollowBack, #InstantFollowBack, #AutoFollowBack, #100ADAY, #500ADAY, #1000ADAY</span> <span class="ago">12 minutes ago</span></p></li>
    <li><span class="avatar" role="img" aria-label="User avatar" style="background:#5a3a2a"></span><p><span class="who">ebb_rio_yt:</span> THE END OF HUMANITY -</p></li>
  </ul>
</div>
</body>
</html>
```